Business Cards for an 'affordable luxury' inner city home builder in Calgary.

We need a business card design that emulates the progressive, innovative, culture of our company and the modern style of our homes. Use our website www.velmarcrest-ab.com as a reference for the product we build.

Our company builds homes in the inner city space of Calgary, Alberta. We build affordable luxury.

Target Market(s)

Young professional Families

Contact Information for Business Card

Try to maintain consistency with the logo font and the card font.

Requirements
Must have
• The details must include: Name, education, title, phone number, website and email (Address is not as important)
• The design must be uniques (like our logo), elegant, sophisticated and modern.

```html
<!DOCTYPE html>
<html lang="en">
<head>
<meta charset="utf-8">
<title>Velmarcrest Custom Homes – Business Card</title>
<link rel="stylesheet" href="https://fonts.googleapis.com/css2?family=Open+Sans:wght@400;700&display=swap">
<style>
  :root {
    --backdrop: #2b2b2c;
    --card: #1d1d1e;
    --ink: #f2f2f2;
    --ink-soft: #b9b9bb;
    --groove: #0e0e0f;
    --groove-light: #3c3c3e;
    --mark: #3a3a3c;
  }
  * { box-sizing: border-box; margin: 0; padding: 0; }
  html, body {
    width: 1200px; height: 1000px; overflow: hidden;
    background: var(--backdrop);
    font-family: "Open Sans", Verdana, sans-serif;
  }
  .canvas {
    position: relative; width: 1200px; height: 1000px;
  }
  .card {
    position: absolute; left: 320px; width: 560px; height: 320px;
    background: var(--card);
    box-shadow: 0 14px 30px rgba(0,0,0,0.45);
    overflow: hidden;
  }
  .card--front { top: 140px; }
  .card--back { top: 540px; }
  .card__rule {
    position: absolute; inset: 0; width: 100%; height: 100%;
  }
  .brand-square {
    position: absolute; width: 30px; height: 30px;
    background: var(--mark);
  }
  .card--front .brand-square { left: 128px; top: 178px; }
  .card--back .brand-square { left: 128px; top: 178px; }
  .brand-name {
    position: absolute; left: 176px; top: 112px;
    color: var(--ink); font-weight: 700; font-size: 19px;
    line-height: 21px; letter-spacing: 1.5px; text-transform: uppercase;
  }
  .person {
    position: absolute; left: 176px; top: 150px; color: var(--ink);
  }
  .person__name { font-size: 20px; font-weight: 400; line-height: 24px; }
  .person__detail { font-size: 12px; color: var(--ink-soft); line-height: 16px; padding-left: 8px; }
  .contact {
    position: absolute; left: 370px; top: 68px;
    padding-left: 22px; color: var(--ink-soft);
    font-size: 12.5px; line-height: 19px;
  }
  .contact::before {
    content: ""; position: absolute; left: 0; top: 4px;
    width: 3px; height: 50px; background: var(--groove);
    box-shadow: 1px 0 0 var(--groove-light);
  }
</style>
</head>
<body>
<main class="canvas">
  <section class="card card--front" aria-label="Card front">
    <svg class="card__rule" viewBox="0 0 560 320" aria-hidden="true">
      <polyline points="70,320 158,208 560,168" fill="none" stroke="var(--groove)" stroke-width="3"/>
      <polyline points="71,321 159,210 560,170" fill="none" stroke="var(--groove-light)" stroke-width="1"/>
    </svg>
    <span class="brand-square" aria-hidden="true"></span>
    <h1 class="brand-name">Velmarcrest<br>Custom<br>Homes Ltd</h1>
  </section>

  <section class="card card--back" aria-label="Card back">
    <svg class="card__rule" viewBox="0 0 560 320" aria-hidden="true">
      <polyline points="70,320 158,208 560,168" fill="none" stroke="var(--groove)" stroke-width="3"/>
      <polyline points="71,321 159,210 560,170" fill="none" stroke="var(--groove-light)" stroke-width="1"/>
    </svg>
    <span class="brand-square" aria-hidden="true"></span>
    <div class="person">
      <p class="person__name">Name</p>
      <p class="person__detail">education</p>
      <p class="person__detail">title</p>
    </div>
    <address class="contact" style="font-style:normal">
      <p>www.velmarcrest-ab.com</p>
      <p>403-555-0148</p>
      <p>projects@velmarcrest-ab.com</p>
    </address>
  </section>
</main>
</body>
</html>
```